Chicago Property Management Flyer

We need a brochure/flyer to market our property management services to Chicago property owners. I believe that my preference is single page, double sided, but a bi-fold or tri-fold format may also work. I have provided our logo, and some example images in case that is helpful. Refer to our website at http://www.lumevarpm.net/ for more info.

Industry/Entity Type

Property Management

Font styles to use
Sans Serif

```html
<!DOCTYPE html>
<html lang="en">
<head>
<meta charset="utf-8">
<title>Lumevar Property Management Flyer</title>
<link rel="stylesheet" href="https://fonts.googleapis.com/css2?family=Montserrat:wght@500;700&family=Oswald:wght@400;500;600&family=Open+Sans:wght@300;400;600;700&family=Roboto+Condensed:wght@400;700&display=swap">
<style>
:root{
  --stage:#3a3b3d;
  --paper:#ffffff;
  --brand-blue:#1b7cc4;
  --deep-blue:#1a5a92;
  --logo-blue:#1e5f97;
  --ink-grey:#5a6068;
  --tab-grey:#5b6168;
  --strip-grey:#6e7377;
  --body-white:#e9f2fa;
}
*{margin:0;padding:0;box-sizing:border-box}
html,body{width:1200px;height:852px;overflow:hidden;background:var(--stage)}
.canvas{position:relative;width:1200px;height:852px;background:var(--stage)}
.page{position:absolute;top:66px;width:518px;height:728px;background:var(--paper);overflow:hidden;box-shadow:0 2px 6px rgba(0,0,0,.45)}
.page--front{left:53px}
.page--back{left:598px}
.abs{position:absolute}
.blue-band{position:absolute;left:0;top:146px;width:518px;height:514px;background:var(--brand-blue)}
.band-edge{position:absolute;left:0;top:130px}
.bottom-strip{position:absolute;left:0;bottom:0;width:518px;height:12px;background:var(--strip-grey)}

.brand{position:absolute;text-align:center;white-space:nowrap}
.brand__mark{width:24px;height:24px;background:var(--logo-blue);margin:0 auto 10px}
.brand__name{font-family:'Montserrat',sans-serif;font-weight:700;font-size:19.5px;color:var(--logo-blue);line-height:1}
.brand__sub{font-family:'Montserrat',sans-serif;font-weight:500;font-size:12.5px;color:var(--ink-grey);letter-spacing:4px;margin-top:4px;line-height:1}

.tab{position:absolute;top:136px;height:32px;background:var(--tab-grey);color:#fff;display:flex;align-items:center;justify-content:center;border-radius:3px;box-shadow:0 2px 4px rgba(0,0,0,.35);white-space:nowrap}
.tab--url{left:279px;width:210px;font-family:'Roboto Condensed',sans-serif;font-weight:700;font-size:20px;letter-spacing:1.5px}
.tab--adv{left:35px;width:192px;font-family:'Oswald',sans-serif;font-weight:500;font-size:14.5px}

.headline-front{position:absolute;right:24px;top:26px;text-align:right;font-family:'Oswald',sans-serif;font-weight:600;font-size:22px;line-height:26.5px;color:var(--ink-grey);letter-spacing:.3px}
.headline-back{position:absolute;left:28px;top:28px;font-family:'Oswald',sans-serif;font-weight:400;font-size:20px;line-height:28px;color:var(--ink-grey);letter-spacing:.6px}

.photo{position:absolute;border-radius:6px;border:2px solid rgba(255,255,255,.85);box-shadow:0 2px 5px rgba(0,0,0,.35)}
.photo__label{position:absolute;top:8px;font-family:'Open Sans',sans-serif;font-weight:600;font-size:8px;color:#111;white-space:nowrap}
.photo--brick{left:26px;top:182px;width:288px;height:228px;background:linear-gradient(160deg,#b9c9dc 0%,#9a4a36 35%,#8a3d2c 60%,#5f7a44 85%,#c9c9c4 100%)}
.photo--west{left:318px;top:182px;width:178px;height:228px;background:linear-gradient(180deg,#dfe5ea 0%,#9fa9b3 45%,#6f7a6a 75%,#8b8d85 100%)}
.photo--yellow{left:26px;top:415px;width:229px;height:228px;background:linear-gradient(150deg,#cfd8e2 0%,#c9ae76 35%,#b3945c 70%,#7d7c70 100%)}
.photo--aerial{left:259px;top:415px;width:237px;height:228px;background:linear-gradient(180deg,#d7d7d7 0%,#9a9a9a 40%,#5c5c5c 75%,#3e3e3e 100%)}
.photo--tower{left:314px;top:186px;width:177px;height:286px;background:linear-gradient(170deg,#9fb8d6 0%,#6c7f93 35%,#4b5866 65%,#2f3944 100%)}
.photo--map{left:26px;top:614px;width:129px;height:92px;background:linear-gradient(135deg,#eef0ec 0%,#dfe6ee 55%,#a9cdee 100%);border-radius:5px}

.footer-front{position:absolute;left:0;top:660px;width:518px;height:56px;display:flex;align-items:center;justify-content:center;text-align:center;font-family:'Open Sans',sans-serif;font-weight:400;font-size:17.5px;line-height:21.5px;color:#444}

.benefit{position:absolute;left:14px;width:274px}
.benefit__title{height:20px;background:var(--deep-blue);border-radius:10px;color:#fff;font-family:'Oswald',sans-serif;font-weight:500;font-size:12.5px;line-height:20px;padding-left:11px;letter-spacing:.3px;white-space:nowrap}
.benefit__text{font-family:'Open Sans',sans-serif;font-size:7.6px;line-height:11px;color:var(--body-white);padding:7px 0 0 10px;text-align:justify}

.advantages{position:absolute;left:314px;top:496px;width:177px;height:106px;background:var(--deep-blue);border-radius:5px;padding:6px 0 0 8px;list-style:none}
.advantages li{font-family:'Open Sans',sans-serif;font-size:11px;line-height:16.8px;color:#fff;display:flex;align-items:center;white-space:nowrap}
.advantages li::before{content:"";width:8px;height:8px;border-radius:50%;background:#e6e6e6;margin-right:11px}

.contact{position:absolute;left:216px;top:623px;width:280px;height:39px;background:var(--tab-grey);border-radius:3px 3px 0 0;display:flex;align-items:center;justify-content:center;color:#fff;gap:4px;white-space:nowrap}
.contact__lead{font-family:'Roboto Condensed',sans-serif;font-size:15px}
.contact__phone{font-family:'Roboto Condensed',sans-serif;font-weight:700;font-size:23px}
.contact-lines{position:absolute;left:216px;top:668px;width:280px;text-align:center;font-family:'Open Sans',sans-serif;color:#333;white-space:nowrap}
.contact-lines__email{font-size:15px;line-height:20px}
.contact-lines__email b{font-weight:700}
.contact-lines__addr{font-size:11.5px;line-height:22px}
</style>
</head>
<body>
<div class="canvas">

  <section class="page page--front">
    <div class="blue-band"></div>
    <svg class="band-edge" width="518" height="34" viewBox="0 0 518 34"><polygon points="0,0 518,0 518,16 279,16 249,34 0,34" fill="#fff"/></svg>
    <div class="brand" style="left:22px;top:82px;width:254px">
      <div class="brand__mark"></div>
      <div class="brand__name">LUMEVAR PROPERTY</div>
      <div class="brand__sub">MANAGEMENT</div>
    </div>
    <h1 class="headline-front">MANAGING CHA / SECTION 8<br>RENTALS ACROSS CHICAGO<br>FOR OVER A DECADE</h1>
    <div class="tab tab--url">www.lumevarpm.net</div>

    <div class="photo photo--brick" role="img" aria-label="Red brick apartment buildings on a Chicago South Side street"><span class="photo__label" style="right:8px">Chicago-South-Side-Property-Management</span></div>
    <div class="photo photo--west" role="img" aria-label="Chicago skyline seen from the near west side"><span class="photo__label" style="left:8px">Chicago from near west</span></div>
    <div class="photo photo--yellow" role="img" aria-label="Yellow brick corner apartment building with iron fence"><span class="photo__label" style="left:7px">chicago_real_estate</span></div>
    <div class="photo photo--aerial" role="img" aria-label="Black and white aerial view of downtown Chicago and the lake"><span class="photo__label" style="left:7px">Chicago Lakefront Tower View</span></div>

    <p class="footer-front">Leverage our experience and expertise to<br>succeed with your properties</p>
    <div class="bottom-strip"></div>
  </section>

  <section class="page page--back">
    <div class="blue-band"></div>
    <svg class="band-edge" width="518" height="34" viewBox="0 0 518 34"><polygon points="0,0 518,0 518,34 262,34 234,16 0,16" fill="#fff"/></svg>
    <h2 class="headline-back">LEVERAGE OUR EXPERIENCE AND<br>EXPERTISE TO SUCCEED WITH<br>YOUR PROPERTIES</h2>
    <div class="brand" style="left:262px;top:82px;width:240px">
      <div class="brand__mark"></div>
      <div class="brand__name">LUMEVAR PROPERTY</div>
      <div class="brand__sub">MANAGEMENT</div>
    </div>
    <div class="tab tab--adv">THE LUMEVAR ADVANTAGES</div>

    <div class="benefit" style="top:188px">
      <div class="benefit__title">SAVE TIME AND HEADACHES</div>
      <p class="benefit__text">We have a team in place to tackle all aspects of property management for you. Never worry about leasing, tenants, maintenance, regulations, etc.</p>
    </div>
    <div class="benefit" style="top:260px">
      <div class="benefit__title">MAXIMIZE YOUR INVESTMENT ASSETS</div>
      <p class="benefit__text">Your properties are expensive assets with lots of potential. Put the right professionals in place to protect, maintain, and maximize their value.</p>
    </div>
    <div class="benefit" style="top:323px">
      <div class="benefit__title">INCREASE INCOME</div>
      <p class="benefit__text">With our experience and market knowledge we can establish optimal rent prices, lease apartments quickly, reduce turnover, and navigate complex housing agency processes to ensure.</p>
    </div>
    <div class="benefit" style="top:396px">
      <div class="benefit__title">REDUCE EXPENSES, MAXIMIZE PROFITS</div>
      <p class="benefit__text">Maximize your profits by benefitting from our economies of scale, systems and processes, specialized knowledge, industry network, and buying power.</p>
    </div>
    <div class="benefit" style="top:471px">
      <div class="benefit__title">STAY INFORMED</div>
      <p class="benefit__text">With access to all of your property information, documentation, and financials through your online portal of our property management system you and your accountant can stay informed as needed.</p>
    </div>
    <div class="benefit" style="top:544px">
      <div class="benefit__title">GROW YOUR INVESTMENT PORTFOLIO</div>
      <p class="benefit__text">With our management team focused on profitably managing your existing properties, we can then help you expand to future investments</p>
    </div>

    <div class="photo photo--tower" role="img" aria-label="Glass high-rise tower seen from below against a blue sky"></div>
    <ul class="advantages">
      <li>Experience</li>
      <li>Economies of Scale</li>
      <li>Systems and Processes</li>
      <li>Specialized Knowledge</li>
      <li>Buying Power</li>
      <li>Housing Agency Experts</li>
    </ul>

    <div class="photo photo--map" role="img" aria-label="Street map of Chicago with office location pin"></div>
    <div class="contact"><span class="contact__lead">CONTACT US NOW @:</span><span class="contact__phone">773-555-0148</span></div>
    <div class="contact-lines">
      <p class="contact-lines__email"><b>email:</b> dana@lumevarpm.net</p>
      <p class="contact-lines__addr">1180 W. Harlan Ave, Chicago IL 60608</p>
    </div>
    <div class="bottom-strip"></div>
  </section>

</div>
</body>
</html>
```